Business Card Design Project

I am a Homoeopath and would like a new business card which represents my clinic and how I work...My clinic Thistle Wellness is situated near Calderwood forest, you can hear the lyrebirds calling all the time!
My work is holistic and deals with shifting energy in order to create balance within the body. There is a very strong spiritual element to my work.
I have uploaded my current card, As far as the actual details on the front and the back I would like these to remain in the same structure...

Target Market(s)

those looking for alternative health therapies... all of my patients are referred to me so I am not concerned about fitting into a mainstream box

Industry/Entity Type

Clinic

Requirements
Must have
• This card must not look corporate!
be creative and different

Nice to have
• I am picturing a tree of life with roots heading into the earth and on it is a white peacock, maybe a body of water and a full moon nearby?

```html
<!DOCTYPE html>
<html lang="en">
<head>
<meta charset="utf-8">
<title>Thistle Wellness – Business Card</title>
<link rel="stylesheet" href="https://fonts.googleapis.com/css2?family=Sacramento&family=Montserrat:wght@400;600&display=swap">
<style>
  :root {
    --space-deep: #2a1a4f;
    --space-violet: #5b3f9a;
    --space-magenta: #c2407f;
    --space-rose: #e88ab4;
    --space-blue: #3f6fc2;
    --forest-dark: #3d4a40;
    --forest-mid: #7d8f83;
    --forest-pale: #c9d3cc;
    --bird-pink: #e8b7d4;
    --text-white: #ffffff;
    --text-muted: #9aa3b8;
  }
  html, body {
    margin: 0;
    padding: 0;
    width: 685px;
    height: 1200px;
    overflow: hidden;
    background: #ffffff;
  }
  .card {
    position: relative;
    width: 685px;
    height: 1200px;
    overflow: hidden;
    background:
      radial-gradient(circle at 40% 22%, rgba(255,255,255,0.95) 0, rgba(255,230,245,0.6) 60px, transparent 190px),
      radial-gradient(circle at 15% 70%, rgba(120,170,255,0.55) 0, transparent 260px),
      radial-gradient(circle at 20% 95%, var(--space-blue) 0, transparent 330px),
      radial-gradient(circle at 90% 55%, var(--space-magenta) 0, transparent 340px),
      radial-gradient(circle at 80% 10%, var(--space-rose) 0, transparent 300px),
      radial-gradient(circle at 90% 95%, var(--space-rose) 0, transparent 260px),
      linear-gradient(160deg, var(--space-violet) 0%, var(--space-deep) 45%, var(--space-violet) 75%, var(--space-deep) 100%);
  }
  .brand-name {
    position: absolute;
    top: 78px;
    left: 0;
    width: 100%;
    margin: 0;
    text-align: center;
    white-space: nowrap;
    font-family: "Sacramento", cursive;
    font-weight: 400;
    font-size: 92px;
    line-height: 1;
    color: var(--text-white);
  }
  .tagline {
    position: absolute;
    top: 196px;
    left: 0;
    width: 100%;
    margin: 0;
    text-align: center;
    white-space: nowrap;
    font-family: "Montserrat", sans-serif;
    font-size: 23px;
    letter-spacing: 1px;
    color: var(--text-white);
  }
  .emblem {
    position: absolute;
    left: 100px;
    top: 382px;
    width: 484px;
    height: 484px;
  }
  .contact {
    position: absolute;
    left: 55px;
    top: 980px;
    font-family: "Montserrat", sans-serif;
    color: var(--text-white);
    white-space: nowrap;
  }
  .contact p { margin: 0; }
  .contact-name {
    font-weight: 600;
    font-size: 24px;
    letter-spacing: 0.5px;
  }
  .contact-credentials {
    margin-top: 4px !important;
    font-size: 22px;
    color: var(--text-muted);
  }
  .contact-email {
    margin-top: 28px !important;
    font-size: 22px;
  }
  .contact-phone {
    margin-top: 4px !important;
    font-size: 22px;
  }
</style>
</head>
<body>
  <main class="card">
    <h1 class="brand-name">Thistle Wellness</h1>
    <p class="tagline">— CLASSICAL HOMOEOPATHY —</p>

    <svg class="emblem" viewBox="0 0 484 484" role="img" aria-label="White peacock perched among tall forest trees, set in a circle">
      <defs>
        <radialGradient id="forest-fill" cx="50%" cy="45%" r="60%">
          <stop offset="0%" stop-color="var(--forest-pale)"/>
          <stop offset="45%" stop-color="var(--forest-mid)"/>
          <stop offset="100%" stop-color="var(--forest-dark)"/>
        </radialGradient>
        <radialGradient id="bird-glow" cx="55%" cy="45%" r="40%">
          <stop offset="0%" stop-color="var(--bird-pink)" stop-opacity="0.85"/>
          <stop offset="100%" stop-color="var(--bird-pink)" stop-opacity="0"/>
        </radialGradient>
      </defs>
      <circle cx="242" cy="242" r="242" fill="url(#forest-fill)"/>
      <circle cx="242" cy="242" r="242" fill="url(#bird-glow)"/>
    </svg>

    <section class="contact">
      <p class="contact-name">MAREN HOLLOWAY</p>
      <p class="contact-credentials">Adv Dip Hom Prof Memb Assoc Reg</p>
      <p class="contact-email">maren_holloway@fernmail.com</p>
      <p class="contact-phone">0400-123-987</p>
    </section>
  </main>
</body>
</html>
```